Business card for our large format printing and installation business

We want a professional looking business card for our business. We manufacture and install Signs.

On the back of the card add this info
Large Format Graphics Printing & Installations, Event Graphics, Banners, Posters, Vehicle Fleet Graphics, Boat Wraps, Wall Murals, Decals,Displays,Signs,Plaques,Digital Signs

On the Front of the card add the Tallmoor Signs logo, plus On the back of the card add the Orange Tallmoor Wraps logo. The 2 vector logos are attached to the design brief.

Target Market(s)

Local business owners

Contact Information for Business Card

Colors
f37122
f68d4e
f9ba93

Requirements
Must have
• On the Front of the card add the Tallmoor Signs logo, plus On the back of the card add the Orange Tallmoor Wraps logo. The 2 vector logos are attached to the design brief.

```html
<!DOCTYPE html>
<html lang="en">
<head>
<meta charset="UTF-8">
<title>Tallmoor Signs — Business Card</title>
<link href="https://fonts.googleapis.com/css2?family=Roboto:wght@400;500;700;900&display=swap" rel="stylesheet">
<style>
  :root {
    --bg: #2a2a2a;
    --card: #333333;
    --accent: #f37122;
    --accent-mid: #f68d4e;
    --accent-soft: #f9ba93;
    --text: #ffffff;
    --muted: #e6e6e6;
  }
  * { box-sizing: border-box; margin: 0; padding: 0; }
  html, body {
    width: 1200px; height: 960px; overflow: hidden;
    background: var(--bg);
    font-family: "Roboto", Arial, sans-serif;
  }
  .canvas { position: relative; width: 1200px; height: 960px; }
  .card {
    position: absolute; left: 232px;
    width: 736px; height: 420px;
    background: var(--card);
    border-radius: 22px;
  }
  .card--front { top: 40px; }
  .card--back { top: 500px; }

  .front-brand {
    position: absolute; left: 0; right: 0; top: 150px;
    text-align: center;
    color: var(--accent);
    font-weight: 900; font-size: 64px; line-height: 1;
  }
  .front-web {
    position: absolute; left: 0; right: 0; top: 320px;
    text-align: center;
    color: var(--accent);
    font-size: 18px; letter-spacing: 2px;
  }

  .back-brands {
    position: absolute; left: 50px; top: 82px; width: 280px;
    text-align: center;
  }
  .back-brand {
    color: var(--accent);
    font-weight: 900; font-size: 40px; line-height: 1.05;
  }
  .wraps-brand {
    margin-top: 18px;
    color: var(--accent);
    font-weight: 900; font-size: 24px; line-height: 1.1;
  }
  .divider-v {
    position: absolute; left: 352px; top: 56px;
    width: 2px; height: 190px; background: var(--accent);
  }
  .contact { position: absolute; left: 378px; top: 52px; }
  .contact-name { color: var(--accent); font-weight: 700; font-size: 30px; }
  .contact-role { color: var(--muted); font-size: 19px; margin: 4px 0 12px 26px; }
  .contact-list { list-style: none; }
  .contact-list li {
    display: flex; align-items: center; gap: 10px;
    color: var(--text); font-size: 21px; line-height: 30px;
    margin-left: 22px;
  }
  .contact-list svg { width: 16px; height: 16px; flex: none; }

  .services {
    position: absolute; left: 40px; right: 40px; top: 272px;
    text-align: center;
    color: var(--accent-soft);
    font-size: 14px; line-height: 21px;
  }
  .services strong { color: var(--accent-mid); font-weight: 500; }

  .address-row {
    position: absolute; left: 30px; right: 30px; top: 358px;
    display: flex; align-items: center; gap: 14px;
  }
  .address-row .rule { flex: 1; height: 2px; background: var(--accent); }
  .address { color: var(--text); font-size: 22px; white-space: nowrap; }
</style>
</head>
<body>
<div class="canvas">

  <section class="card card--front" aria-label="Card front">
    <div class="front-brand">Tallmoor Signs</div>
    <div class="front-web">www.tallmoorsigns.com</div>
  </section>

  <section class="card card--back" aria-label="Card back">
    <div class="back-brands">
      <div class="back-brand">Tallmoor<br>Signs</div>
      <div class="wraps-brand">Tallmoor Wraps</div>
    </div>
    <div class="divider-v"></div>
    <div class="contact">
      <div class="contact-name">Dana Whitfield</div>
      <div class="contact-role">Owner</div>
      <ul class="contact-list">
        <li>
          <svg viewBox="0 0 16 16" aria-hidden="true"><path fill="#f37122" d="M3.5 1.5l2.5 3-1.5 1.5c.8 1.8 2.2 3.2 4 4l1.5-1.5 3 2.5-1.5 2.5C7 13.5 2.5 9 1 3z"/></svg>
          240-555-0148
        </li>
        <li>
          <svg viewBox="0 0 16 16" aria-hidden="true"><rect x="1" y="3" width="14" height="10" fill="#f37122"/><path d="M1 3l7 6 7-6" fill="none" stroke="#333" stroke-width="1.4"/></svg>
          hello@tallmoorsigns.com
        </li>
        <li>
          <svg viewBox="0 0 16 16" aria-hidden="true"><circle cx="8" cy="8" r="7" fill="#f37122"/><path d="M1 8h14M8 1c-3 3-3 11 0 14M8 1c3 3 3 11 0 14" fill="none" stroke="#333" stroke-width="1.1"/></svg>
          www.tallmoorsigns.com
        </li>
      </ul>
    </div>
    <p class="services">
      <strong>Large Format Graphics Printing &amp; Installations</strong> · Event Graphics · Banners · Posters<br>
      Vehicle Fleet Graphics · Boat Wraps · Wall Murals · Decals · Displays · Signs · Plaques · Digital Signs
    </p>
    <div class="address-row">
      <span class="rule"></span>
      <span class="address">418 Fernbrook Road, Maryland 21044</span>
      <span class="rule"></span>
    </div>
  </section>

</div>
</body>
</html>
```